Halvern Properties Business Cards

I would like a business card that includes myself and my partner.
Includes: Logo, office #, email, website, our names, our numbers and possibly the address. I would also like the logo to be embossed and the card to be horizontal.
There is a photo of our yard signs to give you an idea of the colors of our business.

Target Market(s)

Everyone in real estate market.
We are in a rural area. Our clientele are from all socioeconomic backgrounds.

Industry/Entity Type

Real Estate Agent

Contact Information for Business Card

Company Name: Halvern Properties
Our Names, Titles & Cell #'s : Marla Halvern-Broker (555).316.4827, Tessa Halvern-Realtor (555).627.9154
Office #: (555).841.2600
Website: halvernproperties-example.com
Joint Email: halvern@halvernproperties-example.com
Office Address: 518B W. Cottonwell Ave.
Cedarholm, XY. 70999

Font styles to use
Serif

Requirements
Must have
• HORIZONTAL, Logo, Myself and my partners names, Our cell #'s, our office #, our website, our email address
Nice to have
• Embossed logo, office address, our titles.

```html
<!DOCTYPE html>
<html lang="en">
<head>
<meta charset="utf-8">
<title>Halvern Properties Business Card</title>
<link rel="stylesheet" href="https://fonts.googleapis.com/css2?family=Libre+Baskerville:wght@400;700&display=swap">
<style>
  :root {
    --backdrop: #e9e6ea;
    --card-white: #ffffff;
    --plum: #432c5a;
    --skyline-grey: #ececee;
    --ink-light: #ffffff;
    --rule: #8a7a9a;
  }
  * { margin: 0; padding: 0; box-sizing: border-box; }
  html, body {
    width: 1200px; height: 835px; overflow: hidden;
    background: var(--backdrop);
    font-family: "Libre Baskerville", Georgia, serif;
  }
  .card {
    position: absolute; left: 100px; top: 131px;
    width: 1000px; height: 572px;
    background: var(--card-white);
    overflow: hidden;
    box-shadow: 0 10px 30px rgba(40, 20, 60, 0.18);
  }
  .skyline {
    position: absolute; left: 0; top: 70px; width: 1000px; height: 300px;
    background: linear-gradient(180deg, rgba(236,236,238,0) 0%, var(--skyline-grey) 45%, var(--skyline-grey) 100%);
  }
  .base-band { position: absolute; left: 0; top: 0; width: 1000px; height: 572px; display: block; }
  .brand {
    position: absolute; left: 330px; top: 70px;
    display: flex; align-items: center; gap: 22px;
    color: var(--plum);
  }
  .brand-mark {
    width: 74px; height: 74px; border-radius: 50%;
    background: var(--plum);
  }
  .brand-name { text-align: center; font-weight: 700; }
  .brand-name .primary {
    display: block; font-size: 52px; letter-spacing: 2px; line-height: 1;
    padding: 0 4px 8px; border-bottom: 2px solid var(--plum);
  }
  .brand-name .secondary {
    display: block; font-size: 32px; line-height: 1.3; padding-top: 4px;
  }
  .agent {
    position: absolute; color: var(--ink-light); text-align: center;
  }
  .agent .name { font-size: 25px; font-weight: 700; letter-spacing: 2px; text-transform: uppercase; }
  .agent .title { font-size: 19px; font-weight: 700; margin-top: 2px; }
  .agent .cell { font-size: 20px; font-weight: 700; letter-spacing: 1px; margin-top: 2px; }
  .agent-broker { left: 150px; top: 232px; }
  .agent-realtor { left: 560px; top: 340px; }
  .divider {
    position: absolute; left: 520px; top: 305px; width: 2px; height: 70px;
    background: var(--rule); transform: rotate(12deg);
  }
  .contact {
    position: absolute; display: flex; align-items: center; gap: 14px;
    color: var(--ink-light); font-size: 17px; font-weight: 700; letter-spacing: 0.5px;
    white-space: nowrap;
  }
  .contact svg { width: 30px; height: 30px; flex: none; }
  .contact-office { left: 70px; top: 333px; }
  .contact-web { left: 70px; top: 378px; }
  .contact-email { left: 420px; top: 440px; }
  .contact-address { left: 420px; top: 485px; }
</style>
</head>
<body>
  <main class="card">
    <div class="skyline" role="img" aria-label="Faint city skyline silhouette behind the logo"></div>
    <svg class="base-band" width="1000" height="572" viewBox="0 0 1000 572" aria-hidden="true">
      <path d="M0,200 Q430,150 1000,355 L1000,572 L0,572 Z" fill="var(--plum)"/>
    </svg>

    <div class="brand">
      <span class="brand-mark"></span>
      <div class="brand-name">
        <span class="primary">HALVERN</span>
        <span class="secondary">Properties</span>
      </div>
    </div>

    <section class="agent agent-broker">
      <p class="name">Marla Halvern</p>
      <p class="title">Broker</p>
      <p class="cell">(555).316.4827</p>
    </section>

    <span class="divider"></span>

    <section class="agent agent-realtor">
      <p class="name">Tessa Halvern</p>
      <p class="title">Realtor</p>
      <p class="cell">(555).627.9154</p>
    </section>

    <p class="contact contact-office">
      <svg viewBox="0 0 30 30" aria-hidden="true"><circle cx="15" cy="15" r="14" fill="#fff"/><rect x="10" y="8" width="10" height="14" rx="2" fill="var(--plum)"/><rect x="12" y="10" width="6" height="8" fill="#fff"/></svg>
      (555).841.2600
    </p>
    <p class="contact contact-web">
      <svg viewBox="0 0 30 30" aria-hidden="true"><circle cx="15" cy="15" r="14" fill="#fff"/><g fill="none" stroke="var(--plum)" stroke-width="1.6"><circle cx="15" cy="15" r="7"/><ellipse cx="15" cy="15" rx="3" ry="7"/><line x1="8" y1="15" x2="22" y2="15"/></g></svg>
      halvernproperties-example.com
    </p>
    <p class="contact contact-email">
      <svg viewBox="0 0 30 30" aria-hidden="true"><circle cx="15" cy="15" r="14" fill="#fff"/><rect x="8" y="10" width="14" height="10" rx="1" fill="var(--plum)"/><path d="M8,10 L15,16 L22,10" fill="none" stroke="#fff" stroke-width="1.4"/></svg>
      halvern@halvernproperties-example.com
    </p>
    <p class="contact contact-address">
      <svg viewBox="0 0 30 30" aria-hidden="true"><circle cx="15" cy="15" r="14" fill="#fff"/><path d="M15,23 C11,18 10,15 10,13 A5,5 0 0 1 20,13 C20,15 19,18 15,23 Z" fill="var(--plum)"/><circle cx="15" cy="13" r="2" fill="#fff"/></svg>
      518B W. Cottonwell Ave. Cedarholm, XY. 70999
    </p>
  </main>
</body>
</html>
```